Präsentationsvorlagen für Verwaltungsfirma
Zielgruppe
Verwaltungsfirma, IT-Dienstleistungen, Rechnungswesen
Aufgabenstellung
Benötigen Powerpoint Vorlage im Design unserer Farben. inkl. Logo
Benötige das Power Point Format - .pptx

```html
<!DOCTYPE html>
<html lang="de">
<head>
<meta charset="utf-8">
<title>Präsentationsvorlagen – Lumen &amp; Kollegen</title>
<link rel="stylesheet" href="https://fonts.googleapis.com/css2?family=Ubuntu:wght@500;700&family=Open+Sans:wght@400;600;700&display=swap">
<style>
  :root {
    --blue: #1b4fa3;
    --navy: #1f4d86;
    --sky: #1e80f0;
    --paper: #f0f0f0;
    --ink: #2b2b2b;
    --white: #ffffff;
  }
  * { box-sizing: border-box; margin: 0; padding: 0; }
  html, body { width: 1200px; height: 1200px; overflow: hidden; background: var(--white); }
  body { font-family: "Open Sans", Arial, sans-serif; color: var(--ink); }

  .deck {
    position: absolute; left: 77px; top: 68px;
    display: grid;
    grid-template-columns: repeat(3, 285px);
    grid-template-rows: repeat(5, 160px);
    column-gap: 90px; row-gap: 63px;
  }
  .slide { position: relative; width: 285px; height: 160px; background: var(--paper); overflow: hidden; }
  .slide > * { position: absolute; }

  .title { font-family: "Ubuntu", Arial, sans-serif; font-weight: 700; color: var(--blue); line-height: 1; white-space: nowrap; }
  .title.light { color: var(--white); }
  .kicker { font-family: "Open Sans", Arial, sans-serif; font-weight: 600; font-size: 4.2px; letter-spacing: .1px; color: var(--ink); text-transform: uppercase; }
  .kicker.light { color: var(--white); }
  .kicker.blue { color: var(--blue); }
  .para { font-size: 2.9px; line-height: 1.7; color: var(--ink); }
  .para.light { color: var(--white); }
  .para.blue { color: var(--blue); }
  .right { text-align: right; }
  .center { text-align: center; }
  .logo { font-family: "Ubuntu", Arial, sans-serif; font-weight: 500; font-size: 6.2px; letter-spacing: .2px; color: var(--blue); white-space: nowrap; }
  .logo.light { color: var(--white); }

  .panel { background: var(--blue); }
  .panel.navy { background: var(--navy); }
  .box { background: var(--blue); padding: 9px 18px; }
  .box .kicker { display: block; margin-bottom: 2px; }
  .box .para { margin-bottom: 5px; }

  .photo { display: block; }
  .round { border-radius: 50%; }
  .icon { width: 7px; height: 7px; }

  .ph-building { background: linear-gradient(120deg, #1a7ff2 0%, #2a8cf4 45%, #d7e3f0 62%, #2a8cf4 78%); }
  .ph-office   { background: linear-gradient(135deg, #3b4250, #8a6f5c 55%, #c9a88c); }
  .ph-handshake{ background: radial-gradient(circle at 40% 45%, #dfe9f5, #7fa6cf 70%, #3d6797); }
  .ph-target   { background: linear-gradient(160deg, #c9d3dd, #56667a 60%, #9fb0c2); }
  .ph-stairs   { background: radial-gradient(circle at 55% 50%, #2a3640, #b68a5a 45%, #4b5763); }
  .ph-puzzlegl { background: linear-gradient(140deg, #e7eef6, #b9c9dc); }
  .ph-meeting  { background: linear-gradient(90deg, #6d6f73, #c9bfb4 40%, #8a7565 70%, #d6d2cc); }
  .ph-hands    { background: linear-gradient(120deg, #f2f4f7, #c5cdd6 50%, #2c2f36); }
  .ph-bluepz   { background: linear-gradient(135deg, #2a6fd0, #1e5ab6 60%, #4a8ae0); }
  .ph-handpz   { background: linear-gradient(90deg, #ffffff 0%, #f3f3f3 60%, #e2e2e2 80%, #3a3d45 100%); }
  .ph-circuit  { background: radial-gradient(circle at 45% 45%, #6aa0d8, #1d3a78 50%, #0c1733); }
  .ph-shield   { background: linear-gradient(135deg, #1b2a55, #8b6fb8 50%, #2c3f7e); }
  .ph-network  { background: linear-gradient(180deg, #a5805a, #8ea7b0 45%, #6c7d85); }
  .ph-secure   { background: radial-gradient(circle at 50% 45%, #7fd0e8, #3c6fa0 50%, #2a3a55); }
  .ph-light    { background: linear-gradient(160deg, #1a1260 0%, #5b2bd0 30%, #1e6fe0 55%, #7a2ad8 75%, #10104a 100%); }
  .ph-team     { background: linear-gradient(180deg, #c7cdd4, #8c96a3 50%, #39414d); }
  .ph-teamsm   { background: linear-gradient(180deg, #d9dde2, #8e98a5 60%, #3e4652); }
</style>
</head>
<body>
<main class="deck">

  <!-- 1 Cover -->
  <section class="slide">
    <div class="photo ph-building" role="img" aria-label="Bürohochhaus vor blauem Himmel" style="left:0;top:0;width:285px;height:160px;"></div>
    <div class="panel" style="left:10px;top:0;width:117px;height:160px;"></div>
    <h1 class="title light" style="left:23px;top:49px;font-size:10px;line-height:1.3;">PRÄSENTATION<br>SLIDE-VORLAGEN</h1>
    <p class="kicker light" style="left:23px;top:75px;font-size:3.6px;font-weight:400;">Business Presentation Template</p>
    <p class="para light" style="left:23px;top:86px;width:86px;">Wir begleiten Verwaltung, IT-Dienstleistung und Rechnungswesen mit klaren Prozessen und persönlicher Betreuung.</p>
    <span class="logo light" style="left:23px;top:135px;">LUMEN &amp; KOLLEGEN</span>
  </section>

  <!-- 2 Einleitung -->
  <section class="slide">
    <h2 class="title" style="left:22px;top:38px;font-size:12px;">EINLEITUNG</h2>
    <p class="para" style="left:22px;top:55px;width:245px;">Dieser Einleitungstext stellt das Thema der Präsentation kurz vor. Er beschreibt Ausgangslage, Ziele und den Nutzen für Ihre Kunden. Ergänzen Sie hier die wichtigsten Eckdaten Ihres Unternehmens und fassen Sie die Kernaussage in wenigen Sätzen zusammen, damit das Publikum sofort weiß, worum es geht.</p>
    <p class="kicker blue right" style="right:16px;top:101px;font-weight:400;">Unternehmensprofil</p>
    <p class="para blue right" style="right:16px;top:107px;width:80px;">Kurzprofil mit Gründungsjahr, Standorten und Schwerpunkten der Beratung für Verwaltung und IT.</p>
    <span class="logo" style="right:16px;top:131px;">LUMEN &amp; KOLLEGEN</span>
  </section>

  <!-- 3 Über uns -->
  <section class="slide">
    <div class="panel navy" style="left:0;top:0;width:79px;height:160px;"></div>
    <div class="photo ph-office" role="img" aria-label="Foto: Kolleginnen und Kollegen im Büro" style="left:52px;top:0;width:90px;height:127px;"></div>
    <p class="para light center" style="left:10px;top:82px;width:36px;">Seit vielen Jahren Ihr Partner für Verwaltung und Finanzen.</p>
    <h2 class="title right" style="right:20px;top:44px;font-size:12px;">ÜBER UNS</h2>
    <div class="center" style="left:160px;top:67px;width:44px;">
      <p class="kicker blue" style="font-weight:700;">Überschrift</p>
      <p class="para blue">Kurzer Text zu diesem Punkt mit zwei bis drei Zeilen Inhalt.</p>
    </div>
    <div class="center" style="left:211px;top:67px;width:44px;">
      <p class="kicker blue" style="font-weight:700;">Überschrift</p>
      <p class="para blue">Kurzer Text zu diesem Punkt mit zwei bis drei Zeilen Inhalt.</p>
    </div>
    <div class="right" style="right:20px;top:124px;width:80px;">
      <p class="kicker blue" style="font-weight:400;">Überschrift</p>
      <p class="para blue">Ein kurzer Absatz beschreibt hier die Stärken des Teams.</p>
    </div>
  </section>

  <!-- 4 Unsere Mission -->
  <section class="slide">
    <span class="logo" style="left:40px;top:37px;">LUMEN &amp; KOLLEGEN</span>
    <div class="photo ph-handshake round" role="img" aria-label="Foto: Händedruck zweier Geschäftsleute" style="left:21px;top:52px;width:92px;height:92px;"></div>
    <div class="panel" style="left:117px;top:0;width:61px;height:160px;"></div>
    <div class="center" style="left:122px;top:31px;width:51px;">
      <p class="kicker light" style="font-weight:700;">Überschrift</p>
      <p class="para light">Kurzer Text zu diesem Punkt mit zwei bis drei Zeilen Inhalt.</p>
    </div>
    <div class="center" style="left:122px;top:88px;width:51px;">
      <p class="kicker light" style="font-weight:700;">Überschrift</p>
      <p class="para light">Kurzer Text zu diesem Punkt mit zwei bis drei Zeilen Inhalt.</p>
    </div>
    <h2 class="title" style="left:191px;top:38px;font-size:8.6px;">UNSERE MISSION</h2>
    <p class="para right" style="left:200px;top:57px;width:63px;">Unsere Mission ist es, Abläufe in Verwaltung und Rechnungswesen einfacher, sicherer und transparenter zu gestalten – mit Fachwissen, moderner Technik und Verlässlichkeit.</p>
    <p class="para blue right" style="left:205px;top:112px;width:58px;">Ein kurzer Absatz beschreibt hier die Stärken des Teams.</p>
  </section>

  <!-- 5 Unsere Vision -->
  <section class="slide">
    <div class="photo ph-target" role="img" aria-label="Foto: Dartpfeil in Zielscheibe" style="left:25px;top:0;width:62px;height:47px;"></div>
    <div class="photo ph-stairs" role="img" aria-label="Foto: Wendeltreppe von oben" style="left:25px;top:57px;width:62px;height:46px;"></div>
    <div class="photo ph-puzzlegl" role="img" aria-label="Foto: Weltkugel aus Puzzleteilen" style="left:25px;top:114px;width:62px;height:46px;"></div>
    <div class="box" style="left:90px;top:24px;width:120px;height:65px;padding:10px 14px;">
      <h2 class="title light center" style="font-size:10.5px;margin-bottom:6px;">UNSERE VISION</h2>
      <p class="para light center">Wir denken heute an die Lösungen von morgen und gestalten Wandel gemeinsam mit unseren Kunden.</p>
    </div>
    <div class="right" style="left:120px;top:98px;width:84px;">
      <p class="kicker blue" style="font-weight:400;">Überschrift</p>
      <p class="para blue">Ein kurzer Absatz beschreibt hier die Stärken des Teams.</p>
    </div>
    <span class="logo" style="right:86px;top:128px;">LUMEN &amp; KOLLEGEN</span>
    <div class="panel" style="left:215px;top:0;width:70px;height:160px;"></div>
    <div class="center" style="left:222px;top:31px;width:56px;">
      <p class="kicker light" style="font-weight:700;">Überschrift</p>
      <p class="para light">Kurzer Text zu diesem Punkt mit zwei bis drei Zeilen Inhalt.</p>
    </div>
    <div class="center" style="left:222px;top:88px;width:56px;">
      <p class="kicker light" style="font-weight:700;">Überschrift</p>
      <p class="para light">Kurzer Text zu diesem Punkt mit zwei bis drei Zeilen Inhalt.</p>
    </div>
  </section>

  <!-- 6 Unser Service -->
  <section class="slide">
    <h2 class="title" style="left:19px;top:34px;font-size:11px;">UNSER SERVICE</h2>
    <p class="para" style="left:19px;top:49px;width:120px;">Von der Buchhaltung bis zur IT-Betreuung bieten wir Leistungen aus einer Hand, abgestimmt auf Ihre Abläufe.</p>
    <p class="para right" style="left:153px;top:17px;width:88px;">Kurzer Text zu diesem Punkt mit zwei bis drei Zeilen Inhalt.</p>
    <p class="para right" style="left:153px;top:39px;width:88px;">Kurzer Text zu diesem Punkt mit zwei bis drei Zeilen Inhalt.</p>
    <p class="para right" style="left:153px;top:61px;width:88px;">Kurzer Text zu diesem Punkt mit zwei bis drei Zeilen Inhalt.</p>
    <svg class="icon" style="left:256px;top:22px;" viewBox="0 0 24 24" aria-hidden="true"><path d="M2 6h5l10 12h5M2 18h5l3-4M14 10l3-4h5M19 3l3 3-3 3M19 15l3 3-3 3" fill="none" stroke="#111" stroke-width="2"/></svg>
    <svg class="icon" style="left:256px;top:44px;" viewBox="0 0 24 24" aria-hidden="true"><circle cx="12" cy="12" r="11" fill="#111"/><path d="M6.5 12.5l3.5 3.5 7.5-8" fill="none" stroke="#fff" stroke-width="2.6"/></svg>
    <svg class="icon" style="left:256px;top:66px;" viewBox="0 0 24 24" aria-hidden="true"><circle cx="12" cy="12" r="11" fill="#111"/><path d="M12 5l2 4.6 5 .4-3.8 3.3 1.2 4.9L12 15.6 7.6 18.2l1.2-4.9L5 10l5-.4z" fill="#fff"/></svg>
    <div class="box" style="left:0;top:87px;width:139px;height:56px;">
      <p class="kicker light" style="font-weight:400;">Überschrift</p>
      <p class="para light">Ein kurzer Absatz beschreibt hier die Stärken des Teams.</p>
      <span class="logo light">LUMEN &amp; KOLLEGEN</span>
    </div>
    <div class="photo ph-meeting" role="img" aria-label="Foto: Team in einer Besprechungsrunde" style="left:143px;top:87px;width:142px;height:56px;"></div>
  </section>

  <!-- 7 Unser Service (Variante) -->
  <section class="slide">
    <div class="panel" style="left:0;top:0;width:156px;height:160px;"></div>
    <div class="photo ph-hands" role="img" aria-label="Foto: Hände setzen Puzzleteile zusammen" style="left:0;top:0;width:91px;height:69px;"></div>
    <svg class="icon" style="left:100px;top:27px;" viewBox="0 0 24 24" aria-hidden="true"><circle cx="12" cy="12" r="11" fill="#fff"/><path d="M12 5l2 4.6 5 .4-3.8 3.3 1.2 4.9L12 15.6 7.6 18.2l1.2-4.9L5 10l5-.4z" fill="#1b4fa3"/></svg>
    <svg class="icon" style="left:100px;top:67px;" viewBox="0 0 24 24" aria-hidden="true"><path d="M2 6h5l10 12h5M2 18h5l3-4M14 10l3-4h5M19 3l3 3-3 3M19 15l3 3-3 3" fill="none" stroke="#fff" stroke-width="2"/></svg>
    <svg class="icon" style="left:100px;top:108px;" viewBox="0 0 24 24" aria-hidden="true"><circle cx="12" cy="12" r="11" fill="#fff"/><path d="M6.5 12.5l3.5 3.5 7.5-8" fill="none" stroke="#1b4fa3" stroke-width="2.6"/></svg>
    <p class="para light" style="left:117px;top:24px;width:34px;">Kurzer Text zu diesem Punkt.</p>
    <p class="para light" style="left:117px;top:64px;width:34px;">Kurzer Text zu diesem Punkt.</p>
    <p class="para light" style="left:117px;top:104px;width:34px;">Kurzer Text zu diesem Punkt.</p>
    <div style="left:19px;top:96px;width:60px;">
      <p class="kicker light" style="font-weight:400;">Überschrift</p>
      <p class="para light" style="margin-bottom:5px;">Ein kurzer Absatz beschreibt hier die Stärken des Teams.</p>
      <span class="logo light">LUMEN &amp; KOLLEGEN</span>
    </div>
    <h2 class="title" style="left:170px;top:27px;font-size:10.8px;">UNSER SERVICE</h2>
    <p class="para right" style="left:173px;top:42px;width:97px;">Von der Buchhaltung bis zur IT-Betreuung bieten wir Leistungen aus einer Hand, abgestimmt auf Ihre Abläufe.</p>
    <div class="photo ph-bluepz" role="img" aria-label="Foto: blaues Puzzle mit fehlendem Teil" style="left:170px;top:92px;width:115px;height:68px;"></div>
  </section>

  <!-- 8 Lösungen -->
  <section class="slide">
    <h2 class="title" style="left:19px;top:26px;font-size:12.5px;">LÖSUNGEN</h2>
    <p class="para" style="left:19px;top:42px;width:120px;">Wir entwickeln passende Lösungen für komplexe Aufgaben und setzen sie zuverlässig im Alltag um.</p>
    <div class="box" style="left:0;top:87px;width:139px;height:56px;">
      <p class="kicker light" style="font-weight:400;">Überschrift</p>
      <p class="para light">Ein kurzer Absatz beschreibt hier die Stärken des Teams.</p>
      <span class="logo light">LUMEN &amp; KOLLEGEN</span>
    </div>
    <div class="photo ph-handpz" role="img" aria-label="Foto: Hand hält ein blaues Puzzleteil" style="left:149px;top:0;width:136px;height:160px;"></div>
  </section>

  <!-- 9 Lösungen (Variante) -->
  <section class="slide">
    <div class="photo ph-circuit" role="img" aria-label="Illustration: digitales Gehirn auf Leiterplatte" style="left:19px;top:24px;width:116px;height:69px;"></div>
    <div class="box" style="left:146px;top:0;width:139px;height:56px;">
      <p class="kicker light" style="font-weight:400;">Überschrift</p>
      <p class="para light">Ein kurzer Absatz beschreibt hier die Stärken des Teams.</p>
      <span class="logo light">LUMEN &amp; KOLLEGEN</span>
    </div>
    <div class="photo ph-shield" role="img" aria-label="Illustration: Sicherheitsschild über Prozessor" style="left:146px;top:63px;width:115px;height:68px;"></div>
    <h2 class="title" style="left:22px;top:103px;font-size:12.5px;">LÖSUNGEN</h2>
    <p class="para" style="left:22px;top:119px;width:115px;">Wir entwickeln passende Lösungen für komplexe Aufgaben und setzen sie zuverlässig im Alltag um.</p>
  </section>

  <!-- 10 Our Product -->
  <section class="slide">
    <div class="photo ph-network" role="img" aria-label="Foto: Geschäftsmann mit digitalem Netzwerk" style="left:85px;top:0;width:87px;height:160px;"></div>
    <div class="box" style="left:33px;top:92px;width:139px;height:55px;">
      <p class="kicker light" style="font-weight:400;">Überschrift</p>
      <p class="para light">Ein kurzer Absatz beschreibt hier die Stärken des Teams.</p>
      <span class="logo light">LUMEN &amp; KOLLEGEN</span>
    </div>
    <h2 class="title" style="left:185px;top:50px;font-size:12.5px;">Our Product</h2>
    <p class="para" style="left:185px;top:65px;width:80px;">Unser Produkt vereint Sicherheit, Übersicht und einfache Bedienung in einer zentralen Plattform.</p>
  </section>

  <!-- 11 Projekte -->
  <section class="slide">
    <h2 class="title" style="left:36px;top:32px;font-size:10.5px;">PROJEKTE</h2>
    <div class="panel" style="left:32px;top:97px;width:70px;height:63px;"></div>
    <div class="photo ph-secure round" role="img" aria-label="Foto: Hand mit digitalem Sicherheitssymbol" style="left:21px;top:51px;width:92px;height:92px;"></div>
    <p class="para" style="left:127px;top:50px;width:137px;">Ausgewählte Projekte zeigen, wie wir Verwaltungen und Unternehmen bei der Digitalisierung begleitet haben.</p>
    <div class="box" style="left:125px;top:88px;width:140px;height:55px;">
      <p class="kicker light" style="font-weight:400;">Überschrift</p>
      <p class="para light">Ein kurzer Absatz beschreibt hier die Stärken des Teams.</p>
      <span class="logo light">LUMEN &amp; KOLLEGEN</span>
    </div>
  </section>

  <!-- 12 Foto-Folie -->
  <section class="slide">
    <div class="photo ph-light" role="img" aria-label="Foto: blau-violette Lichtspuren" style="left:0;top:0;width:285px;height:160px;"></div>
    <h2 class="title light right" style="right:18px;top:54px;font-size:27px;line-height:1.38;">FOTO<br>FOLIE</h2>
    <div style="left:23px;top:72px;width:90px;">
      <p class="kicker light" style="font-weight:400;">Überschrift</p>
      <p class="para light">Ein kurzer Absatz beschreibt hier die Stärken des Teams.</p>
    </div>
    <span class="logo light" style="left:23px;top:138px;">LUMEN &amp; KOLLEGEN</span>
  </section>

  <!-- 13 Unser Team -->
  <section class="slide">
    <div class="photo ph-team" role="img" aria-label="Foto: Gruppe von Mitarbeitenden im Büro" style="left:21px;top:17px;width:91px;height:125px;"></div>
    <h2 class="title" style="left:127px;top:43px;font-size:12px;">UNSER TEAM</h2>
    <p class="para" style="left:127px;top:58px;width:138px;">Hinter jedem Projekt steht ein erfahrenes Team aus Beratung, Technik und Rechnungswesen.</p>
    <div class="box" style="left:125px;top:86px;width:140px;height:56px;">
      <p class="kicker light" style="font-weight:400;">Business Presentation Template</p>
      <p class="para light">Ein kurzer Absatz beschreibt hier die Stärken des Teams.</p>
      <span class="logo light">LUMEN &amp; KOLLEGEN</span>
    </div>
  </section>

  <!-- 14 Team -->
  <section class="slide">
    <div class="photo ph-teamsm" role="img" aria-label="Foto: Geschäftsteam stehend" style="left:25px;top:0;width:62px;height:47px;"></div>
    <div class="photo ph-teamsm" role="img" aria-label="Foto: drei Mitarbeitende nebeneinander" style="left:25px;top:57px;width:62px;height:46px;"></div>
    <div class="photo ph-teamsm" role="img" aria-label="Foto: Team in hellem Büro" style="left:25px;top:113px;width:62px;height:47px;"></div>
    <h2 class="title right" style="right:19px;top:43px;font-size:13px;">TEAM</h2>
    <p class="para right" style="right:19px;top:58px;width:138px;">Hinter jedem Projekt steht ein erfahrenes Team aus Beratung, Technik und Rechnungswesen.</p>
    <div class="box right" style="left:129px;top:86px;width:139px;height:56px;">
      <p class="kicker light" style="font-weight:400;">Überschrift</p>
      <p class="para light">Ein kurzer Absatz beschreibt hier die Stärken des Teams.</p>
      <span class="logo light">LUMEN &amp; KOLLEGEN</span>
    </div>
  </section>

  <!-- 15 Dankeschön -->
  <section class="slide">
    <p class="kicker blue center" style="left:0;top:61px;width:285px;font-weight:400;">Überschrift</p>
    <h2 class="title center" style="left:0;top:70px;width:285px;font-size:28px;">DANKESCHÖN</h2>
    <p class="para blue center" style="left:92px;top:102px;width:101px;">Vielen Dank für Ihre Aufmerksamkeit und das Interesse.</p>
    <span class="logo" style="left:0;top:134px;width:285px;text-align:center;">LUMEN &amp; KOLLEGEN</span>
  </section>

</main>
</body>
</html>
```